Customs House descriptive business cards

We require a two-sided business card that has a simple yet elegant design. We want to be able to promote our services as a customs house. This card should include our logo, contact info and services offered with the logo being on one side and the contact info and services on the flip side

Target Market(s)

Importers / exporters to and from the Bahamas

Industry/Entity Type

Logistics

Contact Information for Business Card

The front side of the card could have the logo and the flip side should have the other relevant info

Font styles to use
Serif

Colors

Designer to choose colors to be used in the design.

Requirements
Must have
• (Kelpway Brokers Ltd) Logo, address and contact info also services:
• import customs clearance, Delivery & HAndling services,Florida pickups, Export packing & Crating Services, export customs clearance, Consulting

```html
<!DOCTYPE html>
<html lang="en">
<head>
<meta charset="utf-8">
<title>Kelpway Brokers Ltd – Business Card</title>
<link rel="stylesheet" href="https://fonts.googleapis.com/css2?family=Playfair+Display:wght@700&family=Libre+Baskerville:wght@400;700&family=Open+Sans:wght@400&display=swap">
<style>
  :root {
    --brand-blue: #1f7fc4;
    --brand-blue-dark: #1766a8;
    --accent-bar: #4f63b0;
    --ink: #1b1b1b;
    --muted: #555b63;
    --paper: #fbfbfb;
    --backdrop: #e9ecef;
  }
  * { box-sizing: border-box; margin: 0; padding: 0; }
  html, body { width: 1200px; height: 900px; overflow: hidden; }
  body {
    background: var(--backdrop);
    position: relative;
    font-family: "Libre Baskerville", Georgia, serif;
  }
  .card {
    position: absolute;
    left: 260px;
    width: 680px;
    height: 388px;
    background: var(--paper);
    box-shadow: 0 6px 18px rgba(0,0,0,0.12);
    overflow: hidden;
  }
  .card--services { top: 40px; }
  .card--contact { top: 472px; }

  /* Services side */
  .services-frame {
    position: absolute;
    inset: 18px;
    border: 6px solid var(--brand-blue);
  }
  .brand {
    position: absolute;
    display: flex;
    align-items: center;
    gap: 10px;
  }
  .brand__dot {
    width: 18px; height: 18px;
    border-radius: 50%;
    background: var(--brand-blue);
  }
  .brand__name {
    font-family: "Playfair Display", Georgia, serif;
    font-weight: 700;
    font-size: 30px;
    line-height: 1.1;
    color: var(--brand-blue);
    letter-spacing: 0.5px;
  }
  .card--services .brand { left: 62px; top: 168px; width: 280px; }
  .service-list {
    position: absolute;
    left: 370px;
    top: 92px;
    list-style: none;
    font-family: "Open Sans", Arial, sans-serif;
    font-size: 15px;
    color: var(--muted);
  }
  .service-list li {
    display: flex;
    align-items: center;
    gap: 16px;
    height: 34px;
  }
  .service-list svg { width: 16px; height: 20px; flex: none; }

  /* Contact side */
  .contact-bands { position: absolute; inset: 0; }
  .card--contact .brand { left: 70px; top: 168px; width: 280px; }
  .person {
    position: absolute;
    right: 52px;
    top: 62px;
    text-align: right;
    padding-right: 20px;
    border-right: 6px solid var(--accent-bar);
  }
  .person__name {
    font-family: "Playfair Display", Georgia, serif;
    font-weight: 700;
    font-size: 26px;
    letter-spacing: 1px;
    color: var(--ink);
  }
  .person__title {
    margin-top: 6px;
    font-size: 12px;
    letter-spacing: 3px;
    color: var(--brand-blue);
  }
  .contact-details {
    position: absolute;
    left: 420px;
    top: 168px;
    color: var(--ink);
  }
  .contact-row {
    display: flex;
    align-items: flex-start;
    gap: 14px;
    margin-bottom: 10px;
  }
  .contact-row svg { width: 16px; height: 18px; flex: none; margin-top: 2px; }
  .address {
    font-size: 12.5px;
    letter-spacing: 2.5px;
    line-height: 1.55;
    text-transform: uppercase;
  }
  .phone {
    font-family: "Open Sans", Arial, sans-serif;
    font-size: 15px;
  }
  .social-handle, .website {
    position: absolute;
    color: #fff;
    font-family: "Open Sans", Arial, sans-serif;
    font-size: 15px;
    letter-spacing: 1.5px;
  }
  .social-handle { left: 116px; bottom: 14px; }
  .website { right: 26px; bottom: 12px; }
</style>
</head>
<body>

<section class="card card--services" aria-label="Services side">
  <div class="services-frame"></div>
  <div class="brand">
    <span class="brand__dot"></span>
    <span class="brand__name">Kelpway Brokers Ltd</span>
  </div>
  <ul class="service-list">
    <li><svg viewBox="0 0 16 20"><path d="M4 1h8v2l-1 1v5l3 3H2l3-3V4L4 3z M7 12h2v7H7z" fill="#1f7fc4"/></svg>Import customs clearance</li>
    <li><svg viewBox="0 0 16 20"><path d="M4 1h8v2l-1 1v5l3 3H2l3-3V4L4 3z M7 12h2v7H7z" fill="#1f7fc4"/></svg>Delivery &amp; HAndling services</li>
    <li><svg viewBox="0 0 16 20"><path d="M4 1h8v2l-1 1v5l3 3H2l3-3V4L4 3z M7 12h2v7H7z" fill="#1f7fc4"/></svg>Florida pickups</li>
    <li><svg viewBox="0 0 16 20"><path d="M4 1h8v2l-1 1v5l3 3H2l3-3V4L4 3z M7 12h2v7H7z" fill="#1f7fc4"/></svg>Export packing &amp; Crating Services</li>
    <li><svg viewBox="0 0 16 20"><path d="M4 1h8v2l-1 1v5l3 3H2l3-3V4L4 3z M7 12h2v7H7z" fill="#1f7fc4"/></svg>Export customs clearance</li>
    <li><svg viewBox="0 0 16 20"><path d="M4 1h8v2l-1 1v5l3 3H2l3-3V4L4 3z M7 12h2v7H7z" fill="#1f7fc4"/></svg>Consulting</li>
  </ul>
</section>

<section class="card card--contact" aria-label="Contact side">
  <svg class="contact-bands" viewBox="0 0 680 388" preserveAspectRatio="none">
    <polygon points="0,0 680,0 680,70 650,30 0,30" fill="#1f7fc4"/>
    <polygon points="0,300 40,338 680,352 680,388 0,388" fill="#1f7fc4"/>
  </svg>
  <div class="brand">
    <span class="brand__dot"></span>
    <span class="brand__name">Kelpway Brokers Ltd</span>
  </div>
  <div class="person">
    <p class="person__name">DORIAN MACKEY</p>
    <p class="person__title">OPERATIONS DIRECTOR</p>
  </div>
  <div class="contact-details">
    <div class="contact-row">
      <svg viewBox="0 0 16 20"><path d="M8 1a6 6 0 0 1 6 6c0 4.5-6 12-6 12S2 11.5 2 7a6 6 0 0 1 6-6z" fill="#1f7fc4"/><circle cx="8" cy="7" r="2.3" fill="#fff"/></svg>
      <p class="address">42 Seagrape Lane<br>P.O. Box SP-70412<br>Nassau, Bahamas</p>
    </div>
    <div class="contact-row">
      <svg viewBox="0 0 16 18"><rect x="1" y="6" width="14" height="10" rx="2" fill="#1f7fc4"/><path d="M1 6c0-4 14-4 14 0l-3 1H4z" fill="#1f7fc4"/><circle cx="8" cy="11" r="2.5" fill="#fff"/></svg>
      <p class="phone">(242) 555-0147</p>
    </div>
    <div class="contact-row">
      <svg viewBox="0 0 16 18"><path d="M3 1l3 3-1.5 2.5c1 2.5 3 4.5 5.5 5.5L12.5 10.5l3 3-2 3C7 16 1 10 1 3z" fill="#1f7fc4"/></svg>
      <p class="phone">(242) 555-0183</p>
    </div>
  </div>
  <p class="social-handle">@kelpwaybrokersltd</p>
  <p class="website">www.kelpwaybrokersltd.com</p>
</section>

</body>
</html>
```